independent cleaner, reliable, custom, thorough, trustworthy

Not sure yet if I want single-sided or double sided, so I'm selecting double-sided just in case, but single-sided designs are okay.

Really looking to find the happy medium between personal and professional in a business card design. I end up building comfortable relationships with the people I work for.

Most of my business is through referrals, but I want some business cards to hand out to people who ask for one (and maybe put them on community bulletin boards).

My target market is homeowners and business owners who are looking for a reliable cleaner and are willing to pay a bit more to have excellent quality and someone they trust.

Theme: I have a personal-professional feel since I'm solo, so the theme should reflect that. Trustworthy, personal, simple. I clean up messes.

Hopefully this is enough info, let me know if you have any questions though of course!

Target Market(s)

Homeowners businessowners who are looking for a reliable cleaner, excellent quality trustworthy.

Industry/Entity Type

Cleaning Service

Contact Information for Business Card

Please include this text:
• Delphine Marrow
• independent cleaner
• reliable, custom, thorough
• 604-317-2296
• tbw.marrow@quillpost.net

Font styles to use
Serif
Sans Serif

Colors
ffffff
00a990
0492cd
33a6d7
0355a3
3276b5
919191

Requirements
Must have
• Really looking to find the happy medium between personal and professional in a business card design.
• Background: at least 50% white on the side with the most text (coloured accents or shapes are okay)
• I lean more towards simple and clean, solid colours, maybe a gentle gradient
Nice to have
• Not sure yet if I want single-sided or double sided, so I'm selecting double-sided just in case, but single-sided designs are okay.
• Colours: preferably blues and teals for the font and other objects (if any). Open to designer's choice though. I've toyed around with orangey-yellow, but it doesn't feel right and I keep going back to blues/teals
• Also I uploaded a sketch of my signature and initials so you can get a feel for my personality. I'm not expecting this to be included in the design, it's just there.
Should not have
• I don't like a lot of busy-ness or textures
• Also I don't have a logo (not sure where else to specify this)

```html
<!DOCTYPE html>
<html lang="en">
<head>
<meta charset="utf-8">
<title>Delphine Marrow – Business Card</title>
<link rel="stylesheet" href="https://fonts.googleapis.com/css2?family=Roboto:wght@300;400&display=swap">
<style>
  :root {
    --teal: #00a990;
    --grey: #919191;
    --grey-light: #d4d4d4;
    --white: #ffffff;
    --backdrop: #2a2a2e;
    --card-w: 540px;
    --card-h: 309px;
  }
  * { margin: 0; padding: 0; box-sizing: border-box; }
  html, body {
    width: 1200px; height: 800px; overflow: hidden;
    background: var(--backdrop);
    font-family: "Roboto", Arial, sans-serif;
  }
  .stage {
    width: 1200px; height: 800px;
    display: flex; align-items: center; justify-content: center; gap: 40px;
  }
  .card {
    position: relative;
    width: var(--card-w); height: var(--card-h);
    overflow: hidden;
  }
  .card--front {
    background: var(--teal);
    display: flex; align-items: center; justify-content: center;
  }
  .card--back { background: var(--white); }
  .wordmark {
    font-weight: 300;
    font-size: 48px;
    letter-spacing: 1px;
  }
  .card--front .wordmark { color: var(--white); }
  .card--back .wordmark {
    position: absolute; left: 40px; top: 118px;
    color: var(--teal); font-size: 42px;
  }
  .divider {
    position: absolute; left: 262px; top: 44px;
    width: 1px; height: 120px;
    background: var(--grey-light);
  }
  .contact {
    position: absolute; left: 282px; top: 44px;
    line-height: 1.2;
  }
  .contact__name {
    color: var(--grey); font-size: 15px; font-weight: 400;
    text-transform: uppercase; letter-spacing: 0.2px;
  }
  .contact__role { color: var(--teal); font-size: 13px; margin-bottom: 14px; }
  .contact__line {
    display: flex; align-items: center; gap: 6px;
    color: var(--grey); font-size: 12px; margin-bottom: 2px;
  }
  .contact__line svg { width: 10px; height: 10px; fill: var(--teal); }
  .contact__values {
    color: var(--teal); font-size: 13px; margin-top: 12px;
  }
  .wave { position: absolute; left: 0; top: 0; }
</style>
</head>
<body>
<main class="stage">
  <section class="card card--front" aria-label="Card front">
    <span class="wordmark">Marrow</span>
  </section>

  <section class="card card--back" aria-label="Card back">
    <span class="wordmark">Marrow</span>
    <div class="divider"></div>
    <div class="contact">
      <h1 class="contact__name">Delphine Marrow</h1>
      <p class="contact__role">independent cleaner</p>
      <p class="contact__line">
        <svg viewBox="0 0 10 10" aria-hidden="true"><path d="M2 0.5 L3.6 2.6 L2.7 3.6 Q3.8 6 6.4 7.3 L7.4 6.4 L9.5 8 L8.2 9.5 Q4 9 1.5 5.8 Q0.3 3.6 0.6 1.8 Z"/></svg>
        604-317-2296
      </p>
      <p class="contact__line">
        <svg viewBox="0 0 10 10" aria-hidden="true"><path d="M0.5 2 H9.5 V8.5 H0.5 Z M1 2.4 L5 5.6 L9 2.4" stroke="#fff" stroke-width="0.7"/></svg>
        tbw.marrow@quillpost.net
      </p>
      <p class="contact__values">Reliable | Custom | Thorough</p>
    </div>
    <svg class="wave" width="540" height="309" viewBox="0 0 540 309" aria-hidden="true">
      <path d="M150 309 C300 290 360 240 420 190 C460 160 500 140 540 132 L540 309 Z" fill="var(--teal)"/>
      <path d="M120 309 C280 282 345 228 408 178 C450 146 495 124 540 114 L540 122 C497 132 455 152 414 184 C352 234 290 290 142 309 Z" fill="var(--grey)"/>
    </svg>
  </section>
</main>
</body>
</html>
```